Branvique needs a business Card Design

We are looking for a business card Design for our new Managed Service Provider Company, Branvique. Branvique encompasses everything IT for the average medium sized business. Our primary services are help desk support, cyber-security (malware and ransomware protection), and Disaster Recovery systems. We would like the design to have a very clean and professional look, with a very minimalist feel.

Target Market(s)

Medium to large sized businesses

Industry/Entity Type

It Service

Contact Information for Business Card

Name GoesHere
name@branvique.com
O: 555-382-6047
C: 555-731-5820

Font styles to use
Other font styles liked:
• Poppins Font Only Please

Colors

Designer to choose only greyscale colors for use in the design.

Requirements
Must have
• Logo included
Nice to have
• Cutting Edge, innovative, minimalistic, elegant

```html
<!DOCTYPE html>
<html lang="en">
<head>
<meta charset="UTF-8">
<title>Branvique Business Card</title>
<link href="https://fonts.googleapis.com/css2?family=Poppins:wght@300;400;600&display=swap" rel="stylesheet">
<style>
  :root {
    --backdrop: #2b2b2b;
    --card: #1f1f1f;
    --card-edge: #262626;
    --ink-bright: #e6e6e6;
    --ink-soft: #a9a9a9;
    --ink-dim: #5a5a5a;
    --rule: #4a4a4a;
  }
  html, body {
    margin: 0;
    width: 1200px;
    height: 901px;
    overflow: hidden;
    background: var(--backdrop);
    font-family: "Poppins", sans-serif;
  }
  .stage {
    position: relative;
    width: 1200px;
    height: 901px;
  }
  .card {
    position: absolute;
    left: 320px;
    width: 560px;
    height: 320px;
    background: var(--card);
    border: 1px solid var(--card-edge);
    box-shadow: 0 14px 30px rgba(0,0,0,.45);
    box-sizing: border-box;
  }
  .card--front { top: 110px; }
  .card--back { top: 470px; }

  .brand-name {
    position: absolute;
    right: 44px;
    bottom: 44px;
    margin: 0;
    font-weight: 400;
    font-size: 30px;
    letter-spacing: 14px;
    color: var(--ink-bright);
  }

  .identity {
    position: absolute;
    left: 92px;
    top: 112px;
    width: 150px;
    text-align: right;
  }
  .identity__name {
    margin: 0;
    font-weight: 600;
    font-size: 22px;
    line-height: 1.1;
    color: var(--ink-dim);
    text-transform: uppercase;
    letter-spacing: -0.5px;
  }
  .identity__role {
    margin: 2px 0 0;
    font-weight: 300;
    font-size: 14px;
    color: var(--ink-dim);
  }
  .divider {
    position: absolute;
    left: 262px;
    top: 104px;
    width: 1px;
    height: 74px;
    background: var(--rule);
  }
  .contacts {
    position: absolute;
    left: 280px;
    top: 102px;
    margin: 0;
    padding: 0;
    list-style: none;
  }
  .contacts__item {
    display: flex;
    align-items: center;
    gap: 8px;
    font-weight: 300;
    font-size: 16px;
    line-height: 26px;
    color: var(--ink-bright);
  }
  .contacts__icon {
    width: 13px;
    height: 13px;
    fill: var(--ink-soft);
  }
  .website {
    position: absolute;
    left: 0;
    right: 0;
    bottom: 38px;
    margin: 0;
    text-align: center;
    font-weight: 300;
    font-size: 16px;
    color: var(--ink-soft);
  }
</style>
</head>
<body>
<main class="stage">
  <section class="card card--front" aria-label="Card front">
    <p class="brand-name">BRANVIQUE</p>
  </section>

  <section class="card card--back" aria-label="Card back">
    <div class="identity">
      <p class="identity__name">Alex Morrow</p>
      <p class="identity__role">Manager</p>
    </div>
    <div class="divider"></div>
    <ul class="contacts">
      <li class="contacts__item">
        <svg class="contacts__icon" viewBox="0 0 16 16" aria-hidden="true"><path d="M3.5 1l2.5 3-1.5 1.5c.8 2 2.5 3.7 4.5 4.5L10.5 8.5l3 2.5-1.5 3C7 14 2 9 2 2.5z"/></svg>
        555-382-6047
      </li>
      <li class="contacts__item">
        <svg class="contacts__icon" viewBox="0 0 16 16" aria-hidden="true"><path d="M4.5 0h7a1 1 0 0 1 1 1v14a1 1 0 0 1-1 1h-7a1 1 0 0 1-1-1V1a1 1 0 0 1 1-1zm.5 2v10h6V2zm3 11a1 1 0 1 0 0 2 1 1 0 0 0 0-2z"/></svg>
        555-731-5820
      </li>
      <li class="contacts__item">
        <svg class="contacts__icon" viewBox="0 0 16 16" aria-hidden="true"><path d="M1 3h14v10H1zm1 1.2v.3l6 4 6-4v-.3zM2 6v6h12V6l-6 4z"/></svg>
        alex@branvique.com
      </li>
    </ul>
    <p class="website">www.branvique.com</p>
  </section>
</main>
</body>
</html>
```